Membership card design for video game arena

I need a two sided design for membership cards for my customers. It needs to have instructions on how to book on one side, and a nice catchy design for the other.

Please pull logo and whatever you desire from the website www.brivomund.com

Industry/Entity Type

Entertainment

Contact Information for Business Card

The front must say Brivo-Mund with the address and whatever design you choose. The back must have the details below

Colors

Designer to choose colors to be used in the design.

Requirements
Must have
• Frontside
• Company name address and phone number
• Backside
• Booking Instructions
• www.Brivo-Mund.com/book-now
• Click on General Admission and input information
• Use code Clubpass7 to gain access
• See you there!
Nice to have
• A nice design and whatever you find is pertinent
Should not have
• Useless info

```html
<!DOCTYPE html>
<html lang="en">
<head>
<meta charset="utf-8">
<title>Brivo-Mund Membership Card</title>
<link href="https://fonts.googleapis.com/css2?family=Lato:wght@400;700;900&display=swap" rel="stylesheet">
<style>
  :root{
    --maroon:#6e1e27;
    --maroon-deep:#5a1820;
    --charcoal:#333233;
    --ink-light:#ffffff;
    --page:#e6e6e6;
  }
  html,body{margin:0;padding:0;overflow:hidden;}
  body{width:1200px;height:1200px;background:var(--page);position:relative;font-family:'Lato',sans-serif;color:var(--ink-light);}
  .card{position:absolute;left:186px;width:890px;height:534px;overflow:hidden;
    background:linear-gradient(180deg,var(--maroon) 0%,#5a3334 25%,var(--charcoal) 48%,var(--charcoal) 100%);
    box-shadow:0 18px 24px -14px rgba(0,0,0,.45);}
  .card--front{top:54px;}
  .card--back{top:610px;}

  /* front */
  .brand-mark{position:absolute;left:130px;top:160px;width:300px;text-align:center;
    font-weight:900;font-size:50px;color:var(--maroon);letter-spacing:1px;}
  .divider{position:absolute;left:504px;top:80px;width:2px;height:390px;background:rgba(0,0,0,.35);}
  .name-band{position:absolute;left:506px;top:116px;width:384px;height:87px;background:var(--maroon);
    display:flex;align-items:center;padding-left:40px;box-sizing:border-box;}
  .name-band .name{font-weight:700;font-size:30px;letter-spacing:1.5px;color:var(--ink-light);}
  .contact-row{position:absolute;left:506px;display:flex;align-items:center;font-size:19px;}
  .contact-row .tab{width:22px;height:22px;background:var(--maroon);}
  .contact-row .icon{width:34px;height:34px;border-radius:50%;background:var(--charcoal);border:3px solid var(--maroon);
    margin-left:-2px;display:flex;align-items:center;justify-content:center;}
  .contact-row .text{margin-left:16px;line-height:1.25;}
  .row-phone{top:246px}.row-mail{top:291px}.row-web{top:339px}.row-home{top:389px}

  /* back */
  .frame{position:absolute;left:78px;top:78px;width:738px;height:378px;border:2px solid var(--maroon);border-bottom:none;box-sizing:border-box;}
  .frame-foot{position:absolute;top:454px;height:2px;background:var(--maroon);}
  .frame-foot--left{left:78px;width:212px;}
  .frame-foot--right{left:604px;width:212px;}
  .mini-mark{position:absolute;left:96px;top:118px;font-weight:900;font-size:17px;color:var(--maroon);}
  .heading{position:absolute;left:0;width:890px;text-align:center;}
  .heading .title{font-weight:900;font-size:26px;margin-top:108px;}
  .heading .sub{font-size:18px;text-decoration:underline;margin-top:4px;letter-spacing:.5px;}
  .steps{position:absolute;left:0;top:222px;width:890px;text-align:center;}
  .steps .url{font-size:34px;}
  .steps .line{font-size:25px;margin-top:4px;}
  .steps b{font-weight:900;}
  .activity-strip{position:absolute;left:234px;top:362px;width:414px;height:62px;background:rgba(110,30,39,.35);}
  .sign-off{position:absolute;left:290px;width:314px;top:440px;text-align:center;font-weight:700;font-size:21px;letter-spacing:4px;}
</style>
</head>
<body>
  <section class="card card--front">
    <div class="brand-mark">BRIVO-MUND</div>
    <div class="divider"></div>
    <div class="name-band"><span class="name">BRIVO-MUND</span></div>

    <div class="contact-row row-phone"><span class="tab"></span><span class="icon">
      <svg width="16" height="16" viewBox="0 0 16 16"><path d="M3 2h3l1 3-2 1a9 9 0 0 0 5 5l1-2 3 1v3a1 1 0 0 1-1 1A12 12 0 0 1 2 3a1 1 0 0 1 1-1z" fill="#fff"/></svg>
    </span><span class="text">+1 813-555-0148</span></div>

    <div class="contact-row row-mail"><span class="tab"></span><span class="icon">
      <svg width="16" height="12" viewBox="0 0 16 12"><rect x="0.5" y="0.5" width="15" height="11" fill="none" stroke="#fff"/><path d="M1 1l7 6 7-6" fill="none" stroke="#fff"/></svg>
    </span><span class="text">admin@brivomund.com</span></div>

    <div class="contact-row row-web"><span class="tab"></span><span class="icon">
      <svg width="16" height="16" viewBox="0 0 16 16" fill="none" stroke="#fff" stroke-width="1.2"><circle cx="8" cy="8" r="7"/><ellipse cx="8" cy="8" rx="3" ry="7"/><path d="M1 8h14M2.5 4h11M2.5 12h11"/></svg>
    </span><span class="text">www.brivomund.com</span></div>

    <div class="contact-row row-home"><span class="tab"></span><span class="icon">
      <svg width="16" height="15" viewBox="0 0 16 15"><path d="M8 1l7 6h-2v7H9.5V10h-3v4H3V7H1z" fill="#fff"/></svg>
    </span><span class="text">2716 W Corvel Ave,<br>Tampa FL 33607</span></div>
  </section>

  <section class="card card--back">
    <div class="frame"></div>
    <div class="frame-foot frame-foot--left"></div>
    <div class="frame-foot frame-foot--right"></div>
    <div class="mini-mark">BRIVO-MUND</div>
    <div class="heading">
      <div class="title">BOOKING</div>
      <div class="sub">INSTRUCTIONS</div>
    </div>
    <div class="steps">
      <div class="url">www.Brivo-Mund.com/book-now</div>
      <div class="line"><b>Click</b> on General Admission and input information</div>
      <div class="line">Use <b>code</b> Clubpass7 to gain access</div>
    </div>
    <div class="activity-strip" role="img" aria-label="Row of outline activity icons: runner, game controller, helmet, runner"></div>
    <div class="sign-off">See you there!</div>
  </section>
</body>
</html>
```